Remodeling/Restoration Full Varlow Wrap*

Looking to take current web site and logo and morph all services onto our 2019 Kestral Brava 2400 w Cap. With 24/7 services and eye catching designs.

We are a water and fire restoration company with a strong commercial
services and remodeling background.

Our target market is (residential and commercial properties)

I would like to incorporate blue as that is in our current logo and uniforms

Our website http://k3r.842.webstagebox.com/ is currently being revamped to
display all of our services.

```html
<!DOCTYPE html>
<html lang="en">
<head>
<meta charset="utf-8">
<title>Corvane LLC – Vehicle Wrap Side Panel</title>
<link rel="stylesheet" href="https://fonts.googleapis.com/css2?family=Montserrat:wght@700&family=Oswald:wght@500&display=swap">
<style>
  :root {
    --navy: #12284a;
    --navy-deep: #0c1c36;
    --sky: #8fb4d4;
    --sky-light: #c3d7e8;
    --steel: #4f7ea8;
    --white: #f4f5f6;
    --page: #ffffff;
  }
  * { margin: 0; padding: 0; box-sizing: border-box; }
  html, body { width: 1200px; height: 880px; overflow: hidden; background: var(--page); }
  .wrap-canvas { position: relative; width: 1200px; height: 880px; }
  .wrap-art { position: absolute; left: 0; top: 0; }
  .website {
    position: absolute; left: 70px; top: 462px;
    font: 500 22px/1 "Oswald", sans-serif; color: var(--white); letter-spacing: 0.5px;
  }
  .brand {
    position: absolute; left: 512px; top: 500px; width: 176px;
    display: flex; flex-direction: column; align-items: flex-start;
  }
  .brand-mark { width: 34px; height: 34px; background: var(--steel); margin-bottom: 14px; }
  .brand-name { font: 700 32px/1 "Montserrat", sans-serif; color: var(--navy); white-space: nowrap; }
  .brand-suffix {
    display: flex; align-items: center; gap: 8px; width: 100%; margin-top: 6px;
    font: 700 14px/1 "Montserrat", sans-serif; color: var(--navy);
  }
  .brand-suffix::after { content: ""; flex: 1; height: 2px; background: var(--navy); }
  .services {
    position: absolute; left: 722px; top: 470px; list-style: none;
    font: 500 14px/1.45 "Oswald", sans-serif; color: var(--white); letter-spacing: -0.2px;
  }
  .availability {
    position: absolute; left: 1020px; top: 452px;
    font: 500 16px/1 "Oswald", sans-serif; color: var(--navy);
  }
</style>
</head>
<body>
<main class="wrap-canvas">
  <svg class="wrap-art" width="1200" height="880" viewBox="0 0 1200 880">
    <defs>
      <linearGradient id="glassGradient" x1="0" y1="0" x2="1" y2="1">
        <stop offset="0" stop-color="#6f9cc4"/>
        <stop offset="0.6" stop-color="#a9c6de"/>
        <stop offset="1" stop-color="#7ea6c8"/>
      </linearGradient>
      <linearGradient id="panelGradient" x1="0" y1="0" x2="1" y2="0">
        <stop offset="0" stop-color="#0f2340"/>
        <stop offset="0.55" stop-color="#3e6a93"/>
        <stop offset="1" stop-color="#9cbdd8"/>
      </linearGradient>
    </defs>
    <rect class="wrap-base" x="0" y="160" width="1200" height="560" fill="var(--white)"/>
    <polygon class="glass-photo" role="img" aria-label="Photo of glass office towers in soft blue tones"
             points="0,160 600,160 460,440 0,440" fill="url(#glassGradient)"/>
    <polygon class="navy-field" points="0,440 460,440 320,720 0,720" fill="var(--navy)"/>
    <polygon class="accent-stripe" points="600,160 630,160 490,440 460,440" fill="var(--navy-deep)"/>
    <polygon class="sky-stripe" points="460,440 490,440 350,720 320,720" fill="var(--sky-light)"/>
    <rect class="service-rule" x="700" y="432" width="500" height="14" fill="var(--navy)"/>
    <rect class="service-panel" role="img" aria-label="Photo of an interior space in navy and blue tones"
          x="700" y="446" width="500" height="200" fill="url(#panelGradient)"/>
    <rect class="lower-band" x="700" y="646" width="500" height="74" fill="var(--sky)"/>
  </svg>

  <p class="website">CORVANELLC.COM</p>

  <div class="brand">
    <span class="brand-mark"></span>
    <span class="brand-name">CORVANE</span>
    <span class="brand-suffix">LLC</span>
  </div>

  <ul class="services">
    <li>REMEDIATION</li>
    <li>REMODELING</li>
    <li>PROPERTY MAINTENANCE</li>
    <li>COMMERCIAL CLEANING</li>
    <li>POST CONSTRUCTION SERVICES</li>
    <li>CARPET CLEANING</li>
  </ul>

  <p class="availability">24/7 services</p>
</main>
</body>
</html>
```